Wine Label Design Brisden Vale Red Wine

Design for new wine brand "Brisden Vale". Thinking more of an upscale nautical vibe, or something more classic- old school chateau like.
Red Blend or Cabernet
2018 California
Back label copy:
Brisden Vale encapsulates all the wonder of Brisden Beach on a perfect New England summer day. With one sip, you’ll be transported to the pavilions and boardwalks as you get ready to tighten your sails and head out on the Sound. So pull up a chair and pour a glass as you enjoy the warmth of summer in a glass any time you indulge in this wine.

```html
<!DOCTYPE html>
<html lang="en">
<head>
<meta charset="UTF-8">
<title>Brisden Vale Red Blend Label</title>
<link href="https://fonts.googleapis.com/css2?family=Cinzel:wght@600&family=Libre+Baskerville:wght@400;700&display=swap" rel="stylesheet">
<style>
  :root {
    --backdrop: #b4b4b4;
    --teal: #1f5f78;
    --teal-light: #2a7590;
    --gold: #e6c35c;
    --gold-deep: #c99a2e;
    --gold-text: #ecd58a;
    --wine: #6b2a32;
    --wine-band: #8a1f22;
    --silver: #d9d9db;
    --silver-light: #ececee;
    --ink-brown: #6a3413;
    --cream: #f3e6c8;
  }
  * { margin: 0; padding: 0; box-sizing: border-box; }
  html, body {
    width: 900px;
    height: 1200px;
    overflow: hidden;
    background: var(--backdrop);
  }
  .label {
    position: absolute;
    left: 70px;
    top: 50px;
    width: 760px;
    height: 1100px;
    background: var(--silver);
    overflow: hidden;
  }
  .label__field {
    position: absolute;
    left: 0; top: 0;
    width: 760px;
    height: 800px;
    background: radial-gradient(ellipse at 50% 40%, var(--teal-light), var(--teal) 75%);
  }
  .label__emblem {
    position: absolute;
    left: 210px;
    top: 167px;
    width: 340px;
    height: 340px;
  }
  .label__brand {
    position: absolute;
    left: 0; top: 610px;
    width: 760px;
    text-align: center;
    font-family: "Cinzel", serif;
    font-weight: 600;
    font-size: 82px;
    letter-spacing: 2px;
    color: var(--gold-text);
    line-height: 1;
  }
  .label__variety {
    position: absolute;
    left: 8px; top: 800px;
    width: 744px;
    height: 38px;
    background: linear-gradient(180deg, var(--gold) 0%, #f6dd86 45%, var(--gold-deep) 100%);
    text-align: center;
    font-family: "Libre Baskerville", serif;
    font-size: 27px;
    color: var(--ink-brown);
    line-height: 38px;
  }
  .label__gap {
    position: absolute;
    left: 0; top: 838px;
    width: 760px;
    height: 100px;
    background: linear-gradient(180deg, var(--silver-light), var(--silver));
  }
  .label__vintage {
    position: absolute;
    left: 12px; top: 936px;
    width: 736px;
    height: 104px;
    background: var(--wine-band);
    border-top: 4px solid var(--gold);
    border-bottom: 4px solid var(--gold);
  }
  .label__vintage-text {
    position: absolute;
    left: 0; top: 0;
    width: 100%;
    height: 96px;
    text-align: center;
    font-family: "Libre Baskerville", serif;
    font-weight: 700;
    font-size: 30px;
    color: var(--cream);
    line-height: 96px;
  }
  .label__flourish {
    position: absolute;
    top: 34px;
    width: 110px;
    height: 28px;
    border-radius: 14px;
    background: #5a1416;
  }
  .label__flourish--left { left: 14px; }
  .label__flourish--right { right: 14px; }
  .label__foot {
    position: absolute;
    left: 0; top: 1040px;
    width: 760px;
    height: 60px;
    background: linear-gradient(180deg, var(--silver), var(--silver-light));
  }
</style>
</head>
<body>
  <div class="label">
    <div class="label__field" role="img" aria-label="Teal background with a fine swirling wave pattern"></div>

    <svg class="label__emblem" viewBox="0 0 340 340" xmlns="http://www.w3.org/2000/svg">
      <polygon points="170,4 336,170 170,336 4,170" fill="var(--wine)" stroke="var(--gold)" stroke-width="3"/>
      <polygon points="170,14 326,170 170,326 14,170" fill="url(#emblemGlow)" role="img" aria-label="Engraved pink lighthouse illustration"/>
      <defs>
        <radialGradient id="emblemGlow" cx="50%" cy="50%" r="50%">
          <stop offset="0%" stop-color="#9a4a66"/>
          <stop offset="100%" stop-color="#6b2a32"/>
        </radialGradient>
      </defs>
    </svg>

    <div class="label__brand">Brisden Vale</div>

    <div class="label__variety">Red Blend</div>
    <div class="label__gap"></div>

    <div class="label__vintage">
      <div class="label__flourish label__flourish--left" role="img" aria-label="Dark scroll ornament"></div>
      <div class="label__vintage-text">2018 California</div>
      <div class="label__flourish label__flourish--right" role="img" aria-label="Dark scroll ornament"></div>
    </div>

    <div class="label__foot"></div>
  </div>
</body>
</html>
```